Velmora clinic Website for young modern clinic

Website for velmora clinic
To be modern and sleek.
Clinic base - are young and modern.
Images
Main treatments are Velmora and lip enhancement
Needs to include
Link to Facebook
Link to twitter
Price list
Room for a small brief on each item
Hours
Mon 10-4pm
Tues 10-4pm
Wed 12-8pm
Thurs Fenwick Row 0700-4pm
Friday 10- 2pm
Saturday 9am - 2pm
Booking page/calender
Where we are - map
Address:
52 Marlow Gate, 4 Brindle Lane DT7 4QW
Phone number 0207 394 2816 or 07931548270
Updates
Company Name: MOT
Address: 52 Marlow Gate, 4 Brindle Lane, DT7 4QW
Phone: 0207 394 2816
Website: www.nessawinbournestudio.co.uk
Industry/Entity Type
Clinic
Number of Pages Required
3 page
Look and feel

```html
<!DOCTYPE html>
<html lang="en">
<head>
<meta charset="utf-8">
<title>Nessa Winbourne Aesthetics</title>
<link rel="stylesheet" href="https://fonts.googleapis.com/css2?family=Roboto+Condensed:wght@300;400;700&family=Source+Sans+3:wght@400&display=swap">
<style>
:root{
  --bar-grey:#a6a6aa;
  --text-dark:#333333;
  --nav-grey:#8a8a8e;
  --accent-pink:#f4a9a8;
  --hero-peach:#ecc3ad;
  --hero-light:#fdf9f7;
  --section-grey:#ededed;
  --white:#ffffff;
}
*{margin:0;padding:0;box-sizing:border-box}
html,body{width:1200px;height:1200px;overflow:hidden;background:var(--white)}
body{position:relative;font-family:"Source Sans 3",sans-serif;color:var(--text-dark)}
.top-bar{position:absolute;left:0;top:0;width:1200px;height:45px;background:var(--bar-grey);
  font-family:"Roboto Condensed",sans-serif;font-size:22px;color:var(--white);text-align:right;padding:9px 54px 0 0}
.top-rule{position:absolute;left:0;top:46px;width:1200px;height:4px;background:#f1ebe8}
.site-header{position:absolute;left:0;top:50px;width:1200px;height:115px;background:var(--white);border-bottom:5px solid #f3f1f1}
.brand{position:absolute;left:64px;top:20px;display:flex;align-items:center;gap:12px}
.brand-dot{width:102px;height:78px;border-radius:50%;background:#9c9ca0}
.brand-name{font-family:"Roboto Condensed",sans-serif;font-weight:400;color:#8e8e92;letter-spacing:3px;line-height:1}
.brand-name .line1{display:block;font-size:22px}
.brand-name .line2{display:block;font-size:33px;margin-top:3px}
.main-nav{position:absolute;right:58px;top:33px;display:flex;align-items:center;gap:38px;
  font-family:"Roboto Condensed",sans-serif;font-weight:300;font-size:22px;color:var(--nav-grey)}
.main-nav .active{color:var(--accent-pink)}
.main-nav .cta{background:var(--bar-grey);color:var(--white);font-weight:400;border-radius:22px;padding:7px 34px 7px 20px}
.hero{position:absolute;left:0;top:170px;width:1200px;height:536px;
  background:linear-gradient(180deg,var(--hero-peach) 0%,#f4ddd1 45%,var(--hero-light) 85%,var(--white) 100%)}
.hero-photo{position:absolute;left:480px;top:0;width:680px;height:536px;
  background:radial-gradient(ellipse at 55% 45%,#e7c0a6 0%,#ddb293 35%,rgba(240,214,198,.6) 65%,rgba(253,249,247,0) 85%)}
.hero-copy{position:absolute;left:76px;top:176px;font-family:"Roboto Condensed",sans-serif;color:var(--text-dark)}
.hero-title{font-weight:300;font-size:50px;line-height:49px}
.hero-title strong{font-weight:700}
.hero-sub{font-family:"Source Sans 3",sans-serif;font-size:19px;margin-top:19px}
.hero-book{font-weight:400;font-size:35px;margin-top:4px}
.welcome{position:absolute;left:0;top:706px;width:1200px;height:494px;background:var(--section-grey)}
.welcome-title{position:absolute;left:0;top:34px;width:1162px;text-align:center;font-size:38px;font-weight:400}
.video-frame{position:absolute;left:76px;top:104px;width:472px;height:300px;background:var(--white);border-radius:18px;padding:8px}
.video-placeholder{position:relative;width:100%;height:100%;border-radius:12px;
  background:linear-gradient(180deg,#5a5650 0%,#6d6964 12%,#8d8d8f 26%,#b4aa98 55%,#d9c7a8 100%)}
.play-button{position:absolute;left:181px;top:105px}
.welcome-text{position:absolute;left:590px;top:114px;width:540px;font-size:20px;line-height:25px}
.welcome-text p+p{margin-top:25px}
.contact{position:absolute;left:593px;top:306px;font-size:26px;line-height:32px}
</style>
</head>
<body>
<div class="top-bar">FOR APPOINTMENT&nbsp; : &nbsp;0207 394 2816 OR 07931548270</div>
<div class="top-rule"></div>
<header class="site-header">
  <div class="brand">
    <span class="brand-dot"></span>
    <span class="brand-name"><span class="line1">NESSA WINBOURNE</span><span class="line2">AESTHETICS</span></span>
  </div>
  <nav class="main-nav">
    <span class="active">HOME</span>
    <span>TREATMENTS</span>
    <span>PRICE</span>
    <span class="cta">BOOKING/CALENDER</span>
  </nav>
</header>
<section class="hero">
  <div class="hero-photo" role="img" aria-label="Portrait photo of two smiling women, cheek to cheek"></div>
  <div class="hero-copy">
    <h1 class="hero-title">ACHIEVE A FRESH<br>AND <strong>BEAUTIFUL YOU</strong></h1>
    <p class="hero-sub">LOOKING FOR VELMORA AND LIP ENHANCEMENT</p>
    <p class="hero-book">BOOK YOUR APPOINTMENT NOW</p>
  </div>
</section>
<section class="welcome">
  <h2 class="welcome-title">WELCOME TO NESSA WINBOURNE AESTHETICS</h2>
  <div class="video-frame">
    <div class="video-placeholder" role="img" aria-label="Video still of the clinic shopfront">
      <svg class="play-button" width="74" height="74" viewBox="0 0 74 74" aria-hidden="true">
        <circle cx="37" cy="37" r="36" fill="#ffffff" fill-opacity="0.45"/>
        <polygon points="30,22 53,37 30,52" fill="#5a5650" fill-opacity="0.85"/>
      </svg>
    </div>
  </div>
  <div class="welcome-text">
    <p>Nessa is a registered nurse and independent nurse prescriber with over 7 years experience in cosmetic medicine and facial injections.</p>
    <p>She is a member of the ACAN, NPRC and insured with Hartwell and Moore. She has worked with top plastic surgeons and dermatologists in NZ, Australia and the UK including Fenwick</p>
  </div>
  <div class="contact">
    <p>Phone number 0207 394 2816 or 07931548270</p>
    <p>Email: motbrindlebookings@postmail.co.uk</p>
  </div>
</section>
</body>
</html>
```